Quorvex - Automated robotic Inspection with AI need new business cards

We need a new design of our business cards. The company is focused on automated quality control at high speed with unmatched results. We have a logo but need a more forward leaning business card that shows that we are delivering cutting edge technology.

Contact Information for Business Card

Name
Position
Adress
Phone
Email
e.g.
Lena Holmqvist
Chief Financial Officer (CFO)

Quorvex Sweden AB
Bruksvägen 14, SE-175 43 JÄRFÄLLA, Sweden
Mobile: +46735 21 47 83 | Office: +46 8 61 94 27
www.quorvex-example.com

Font styles to use
Sans Serif

```html
<!DOCTYPE html>
<html lang="en">
<head>
<meta charset="utf-8">
<title>Quorvex business cards</title>
<link rel="stylesheet" href="https://fonts.googleapis.com/css2?family=Roboto:wght@400;500;700&display=swap">
<style>
  :root {
    --brand-blue: #0b5a93;
    --swoosh-grey: #3b4045;
    --ink: #2f3337;
    --card-white: #fbfbfb;
    --backdrop: #cfd0d1;
  }
  * { box-sizing: border-box; margin: 0; padding: 0; }
  html, body { width: 1200px; height: 852px; overflow: hidden; }
  body {
    background: var(--backdrop);
    font-family: "Roboto", Arial, sans-serif;
    position: relative;
  }
  .card {
    position: absolute;
    width: 500px;
    height: 286px;
    background: var(--card-white);
    border-radius: 16px;
    overflow: hidden;
    box-shadow: 0 6px 18px rgba(0,0,0,0.18);
  }
  .card--front { left: 70px; top: 283px; }
  .card--back  { left: 630px; top: 283px; }

  /* front */
  .front-edge {
    position: absolute; left: 0; right: 0; bottom: 0;
    height: 9px; background: var(--brand-blue);
  }
  .brand {
    display: flex; align-items: center; gap: 14px;
    color: var(--brand-blue);
  }
  .brand__dot {
    width: 40px; height: 40px; border-radius: 50%;
    background: var(--brand-blue); flex: none;
  }
  .brand__name {
    font-weight: 700; font-size: 58px; letter-spacing: 1px; line-height: 1;
  }
  .card--front .brand {
    position: absolute; left: 0; right: 0; top: 90px; justify-content: center;
  }
  .front-web {
    position: absolute; left: 0; right: 0; top: 196px;
    display: flex; align-items: center; justify-content: center; gap: 14px;
    font-size: 14px; color: var(--ink);
  }
  .front-web__dash {
    width: 30px; height: 3px; background: var(--brand-blue); border-radius: 2px;
  }

  /* back */
  .wave { position: absolute; inset: 0; }
  .card--back .brand {
    position: absolute; left: 30px; top: 118px; gap: 12px;
  }
  .card--back .brand__dot { width: 28px; height: 28px; }
  .card--back .brand__name { font-size: 40px; }
  .person {
    position: absolute; right: 30px; top: 20px; text-align: right;
    color: var(--ink);
  }
  .person__name {
    font-weight: 700; font-size: 19px; color: var(--brand-blue); margin-bottom: 3px;
  }
  .person__role { font-size: 12.5px; margin-bottom: 8px; }
  .person__address { font-size: 12.5px; line-height: 1.4; }
  .contact {
    position: absolute; right: 26px; top: 186px;
    list-style: none; color: #fff; font-size: 12px; text-align: right;
  }
  .contact li {
    display: flex; align-items: center; justify-content: flex-end; gap: 8px;
    line-height: 1.55;
  }
  .contact svg { width: 12px; height: 12px; flex: none; }
</style>
</head>
<body>

  <section class="card card--front" aria-label="Business card front">
    <div class="brand">
      <span class="brand__dot"></span>
      <span class="brand__name">QUORVEX</span>
    </div>
    <div class="front-web">
      <span class="front-web__dash"></span>
      <span>www.quorvex-example.com</span>
      <span class="front-web__dash"></span>
    </div>
    <div class="front-edge"></div>
  </section>

  <section class="card card--back" aria-label="Business card back">
    <svg class="wave" viewBox="0 0 500 286" preserveAspectRatio="none" aria-hidden="true">
      <path fill="var(--swoosh-grey)"
        d="M0,250 C120,252 220,232 292,192 C352,156 395,132 500,126 L500,136 C400,142 360,164 304,200 C230,246 125,264 0,262 Z"/>
      <path fill="var(--brand-blue)"
        d="M0,286 L0,270 C140,270 250,248 314,206 C366,172 405,152 500,146 L500,286 Z"/>
      <path fill="var(--swoosh-grey)"
        d="M0,274 C90,278 160,274 230,264 C165,280 90,284 0,283 Z"/>
    </svg>

    <div class="person">
      <p class="person__name">Lena Holmqvist</p>
      <p class="person__role">Chief Financial Officer (CFO)</p>
      <p class="person__address">Bruksvägen 14, SE-175<br>43 JÄRFÄLLA, Sweden</p>
    </div>

    <div class="brand">
      <span class="brand__dot"></span>
      <span class="brand__name">QUORVEX</span>
    </div>

    <ul class="contact">
      <li>+46735 21 47 83
        <svg viewBox="0 0 12 12" aria-hidden="true"><path fill="#fff" d="M2.5 1h2l1 2.5-1.3 1a6 6 0 0 0 3.3 3.3l1-1.3 2.5 1v2a1 1 0 0 1-1 1A9.5 9.5 0 0 1 1.5 2a1 1 0 0 1 1-1z"/></svg>
      </li>
      <li>+46 8 61 94 27
        <svg viewBox="0 0 12 12" aria-hidden="true"><path fill="#fff" d="M2.5 1h2l1 2.5-1.3 1a6 6 0 0 0 3.3 3.3l1-1.3 2.5 1v2a1 1 0 0 1-1 1A9.5 9.5 0 0 1 1.5 2a1 1 0 0 1 1-1z"/></svg>
      </li>
      <li>lena.h@quorvex-example.com
        <svg viewBox="0 0 12 12" aria-hidden="true"><rect x="0.5" y="2" width="11" height="8" rx="1" fill="#fff"/><path d="M1 2.6 6 6.5l5-3.9" fill="none" stroke="var(--brand-blue)" stroke-width="1"/></svg>
      </li>
      <li>www.quorvex-example.com
        <svg viewBox="0 0 12 12" aria-hidden="true"><circle cx="6" cy="6" r="5.2" fill="none" stroke="#fff" stroke-width="1.1"/><ellipse cx="6" cy="6" rx="2.2" ry="5.2" fill="none" stroke="#fff" stroke-width="1"/><path d="M1 6h10" stroke="#fff" stroke-width="1"/></svg>
      </li>
    </ul>
  </section>

</body>
</html>
```